Corporate Breakfast Flyer - Breakfast Talk (One Page)

Create a flyer with below using your own selection of content and images from the below. You do not have to use all images I have left them all there for your choice. Please use blue type colors like in our logo. Should be a corporate and professional feel to it.

Venue: Brindlemere Links Club 17 Carrowvale St, Harwick Vale NSW 2190
Date: Thursday the 22nd of September 2016
7.30am: Breakfast and networking
8.00am: Dylan Morrow speaking – Leadership and Motivation
9.00am: Business Card draw and finish

• Mini croissants on arrival – Ham & cheese, tomato & cheese, plain
• Toast station – assorted sliced breads & spreads
• Banana bread slice with honey ricotta
• Chicken & herb chipolata
• Marinated lamb chops
• Creamy scrambled eggs with chives
• Mushroom & cherry tomato kebabs
• Hash browns
• Assorted fruit cocktails with yoghurt & granola, juice station
• Tea and coffee station included
Topic: Leadership and Motivation
Speaker profile (Dylan Morrow):
Dylan Morrow is a four-time Meridian Cup competitor, winning basketball player, coach, entrepreneur, motivational speaker, brand ambassador - and one of Australia's most recognized personalities and sporting figures.
He was the first-ever Australian player to be signed to the PCX from the QVR and he also captained the Harbour Falcons to their first-ever title, helping to raise the profile of basketball around Australia. He has represented Australia at four Meridian Cup and played professionally for more than 20 years in Australia, Europe and the PCX. In February 2012 he was appointed Head Coach of the Harbour Falcons.
Following his retirement from playing, Dylan earned a reputation as a successful entrepreneur and businessman. He built up a successful business in fast food franchising with more than 30 stores across six different brands which, at its peak in 2010, employed over 350 people. After his company was severely affected by the collapse of an KTE listed company in which he had purchased a 10-year contract, Dylan had to start all over again.
Dylan has also held hosting, commentary and columnist roles with WMR, Vista Seven, Orbit Broadcast and Pike Athletics.

Target Market(s)

Finance leaders, Finance Directors, Controllers and CFO's

Font styles to use
Serif
Sans Serif

Colors
33a6d7
0592cd
0355a3
3276b5
85abd2
85cae6

Requirements
Must have
• Must be one page A4 will be sent electronically
Nice to have
• Any other images you feel may be pertinant, I have attached lots of images for you to use for this project please do not use to many. I have attached more so you have more selection
Should not have
• All Images

```html
<!DOCTYPE html>
<html lang="en">
<head>
<meta charset="utf-8">
<title>Leadership &amp; Motivation – Breakfast Talk</title>
<link href="https://fonts.googleapis.com/css2?family=Nunito:wght@700;800;900&family=Roboto+Condensed:wght@400;500&family=PT+Sans:wght@400;700&family=Great+Vibes&display=swap" rel="stylesheet">
<style>
  :root{
    --blue-deep:#0355a3;
    --blue-mid:#3276b5;
    --blue-bright:#0592cd;
    --blue-sky:#33a6d7;
    --blue-soft:#85abd2;
    --blue-pale:#85cae6;
    --ink:#14253a;
    --white:#ffffff;
    --panel-dark:#2b2b2d;
    --gold:#c7b98a;
  }
  *{box-sizing:border-box;margin:0;padding:0}
  html,body{width:848px;height:1200px;overflow:hidden;background:#fff}
  .flyer{
    position:relative;width:848px;height:1200px;overflow:hidden;
    background:
      radial-gradient(circle at 88% 6%, rgba(133,202,230,.55) 0, rgba(133,202,230,0) 32%),
      linear-gradient(160deg,#1a7fd0 0%,var(--blue-bright) 30%,var(--blue-mid) 65%,var(--blue-deep) 100%);
    font-family:"PT Sans",sans-serif;color:var(--white);
  }
  .title{position:absolute;left:46px;top:44px;font-family:"Nunito",sans-serif;font-weight:900;line-height:.9;letter-spacing:-1px}
  .title .line{display:block;font-size:80px}
  .title .amp{position:absolute;left:424px;top:14px;font-family:"Great Vibes",cursive;font-weight:400;font-size:80px;letter-spacing:0}

  .label-bar{position:absolute;left:46px;width:362px;height:27px;padding-left:14px;
    background:linear-gradient(90deg,var(--blue-mid),var(--blue-sky));
    font-family:"Nunito",sans-serif;font-weight:800;font-size:16px;line-height:27px;box-shadow:0 1px 3px rgba(0,0,0,.25)}
  .venue-label{top:200px}
  .date-label{top:426px;width:358px;height:32px;line-height:32px}

  .venue-box{position:absolute;left:46px;top:228px;width:362px;height:82px;background:var(--panel-dark);
    padding:10px 0 0 7px;font-family:"Nunito",sans-serif;font-weight:800;font-size:15.5px;line-height:20px}
  .venue-mark{position:absolute;right:14px;top:30px;display:flex;align-items:center;gap:6px;
    font-family:"PT Sans",sans-serif;font-weight:400;font-size:12px;color:var(--gold);letter-spacing:.5px}
  .venue-mark .dot{width:14px;height:14px;border-radius:50%;background:var(--gold)}

  .venue-photo{position:absolute;left:46px;top:320px;width:362px;height:96px;
    background:linear-gradient(180deg,#0d1626 0%,#1f2c3a 50%,#4a3a22 75%,#1a1a14 100%)}

  .date-text{position:absolute;left:46px;top:468px;font-family:"Nunito",sans-serif;font-weight:800;font-size:18px}

  .schedule{position:absolute;left:46px;top:504px;width:359px;border-collapse:separate;border-spacing:0 2px}
  .schedule td{height:26px;vertical-align:middle;white-space:nowrap}
  .schedule .time{width:74px;padding-left:6px;font-family:"PT Sans",sans-serif;font-size:13.5px;color:var(--white);background:rgba(133,171,210,.35)}
  .schedule .what{padding-left:6px;font-family:"Roboto Condensed",sans-serif;font-weight:500;font-size:12.5px;letter-spacing:-.2px;color:var(--ink);background:var(--blue-pale);border-left:2px solid var(--blue-mid)}

  .menu{position:absolute;left:46px;top:608px;width:360px;list-style:none;font-size:18px;line-height:23px}
  .menu li{position:relative;padding-left:15px;margin-bottom:8.5px}
  .menu li::before{content:"";position:absolute;left:1px;top:9px;width:8px;height:8px;border-radius:50%;background:var(--blue-pale)}

  .speaker-photo{position:absolute;left:470px;top:0;width:360px;height:700px;
    background:radial-gradient(ellipse at 50% 45%,rgba(240,240,240,.55) 0,rgba(220,225,230,.35) 40%,rgba(255,255,255,0) 70%)}

  .profile{position:absolute;left:422px;top:674px;width:394px;height:364px;border-radius:4px;
    background:rgba(133,202,230,.92);padding:6px 12px 0 13px;color:var(--ink)}
  .profile .kicker{font-family:"Nunito",sans-serif;font-weight:800;font-size:20px;color:var(--white);text-shadow:0 1px 2px rgba(0,0,0,.4);line-height:23px}
  .profile .name{font-family:"Nunito",sans-serif;font-weight:900;font-size:31px;color:var(--white);text-shadow:0 1px 3px rgba(0,0,0,.45);line-height:34px;margin-bottom:8px}
  .profile p{font-size:10.8px;line-height:14.6px;margin-bottom:9px;letter-spacing:-.15px}

  .footer-band{position:absolute;left:0;top:1046px;width:848px;height:154px}
  .brand{position:absolute;left:60px;top:1082px;display:flex;align-items:center;gap:16px;
    font-family:"PT Sans",sans-serif;font-weight:400;font-size:46px;color:#3a3f47}
  .brand .dot{width:58px;height:58px;border-radius:50%;background:var(--blue-mid)}
</style>
</head>
<body>
<main class="flyer">
  <div class="speaker-photo" role="img" aria-label="Photo of the speaker dribbling a basketball in a white team uniform"></div>

  <h1 class="title">
    <span class="line">Leadership</span>
    <span class="amp">&amp;</span>
    <span class="line">Motivation</span>
  </h1>

  <div class="label-bar venue-label">Venue:</div>
  <div class="venue-box">
    Brindlemere Links Club<br>17 Carrowvale St,<br>Harwick Vale NSW 2190
    <div class="venue-mark"><span class="dot"></span>BRINDLEMERE LINKS</div>
  </div>
  <div class="venue-photo" role="img" aria-label="Night view of the club house with lit gardens"></div>

  <div class="label-bar date-label">Date:</div>
  <p class="date-text">Thursday the 22nd of September 2016</p>

  <table class="schedule">
    <tr><td class="time">7.30am:</td><td class="what">Breakfast and networking</td></tr>
    <tr><td class="time">8.00am:</td><td class="what">Dylan Morrow speaking – Leadership and Motivation</td></tr>
    <tr><td class="time">9.00am:</td><td class="what">Business Card draw and finish</td></tr>
  </table>

  <ul class="menu">
    <li>Mini croissants on arrival – Ham &amp; cheese, tomato &amp; cheese, plain</li>
    <li>Toast station – assorted sliced breads &amp; spreads</li>
    <li>Banana bread slice with honey ricotta</li>
    <li>Chicken &amp; herb chipolata</li>
    <li>Marinated lamb chops</li>
    <li>Creamy scrambled eggs with chives</li>
    <li>Mushroom &amp; cherry tomato kebabs</li>
    <li>Hash browns</li>
    <li>Assorted fruit cocktails with yoghurt &amp; granola, juice station</li>
    <li>Tea and coffee station included</li>
  </ul>

  <section class="profile">
    <div class="kicker">Speaker profile</div>
    <h2 class="name">Dylan Morrow</h2>
    <p>Dylan Morrow is a four-time Meridian Cup competitor, winning basketball player, coach, entrepreneur, motivational speaker, brand ambassador - and one of Australia's most recognized personalities and sporting figures.</p>
    <p>He was the first-ever Australian player to be signed to the PCX from the QVR and he also captained the Harbour Falcons to their first-ever title, helping to raise the profile of basketball around Australia. He has represented Australia at four Meridian Cup and played professionally for more than 20 years in Australia, Europe and the PCX. In February 2012 he was appointed Head Coach of the Harbour Falcons.</p>
    <p>Following his retirement from playing, Dylan earned a reputation as a successful entrepreneur and businessman. He built up a successful business in fast food franchising with more than 30 stores across six different brands which, at its peak in 2010, employed over 350 people. After his company was severely affected by the collapse of an KTE listed company in which he had purchased a 10-year contract, Dylan had to start all over again.</p>
    <p>Dylan has also held hosting, commentary and columnist roles with WMR, Vista Seven, Orbit Broadcast and Pike Athletics.</p>
  </section>

  <svg class="footer-band" viewBox="0 0 848 154" aria-hidden="true">
    <polygon points="0,0 516,0 552,138 0,138" fill="#ffffff"/>
    <polygon points="425,138 848,138 848,154 425,154" fill="#0a6fc4"/>
    <polygon points="0,138 552,138 556,154 0,154" fill="#ffffff"/>
  </svg>
  <div class="brand"><span class="dot"></span>Calder Wynne</div>
</main>
</body>
</html>
```